Website Header / Banner needed

I need a new Header / Banner to be degigned to replace my current banner at http://www.velvorubtouch.example/banner334.gif

size is 713x 70 pixels (THIS IS THE CORRECT SIZE)

wording is slightly changed ie Velvo Massage 1000,s of UK Escorts & Massage Parlours

Target Market(s)

Adult

Industry/Entity Type

Adult

Logo Text

Velvo Massage 1000's of UK Escorts & Massage Parlours

Requirements
Must have
• size is 713x 70 pixels (THIS IS THE CORRECT SIZE)

```html
<!DOCTYPE html>
<html lang="en">
<head>
<meta charset="utf-8">
<title>Velvo Massage – Header Banner</title>
<link rel="stylesheet" href="https://fonts.googleapis.com/css2?family=Open+Sans:wght@400&display=swap">
<style>
  :root {
    --page-bg: #ebebeb;
    --banner-navy: #06003f;
    --brand-pink: #e8175d;
    --brand-white: #ffffff;
    --photo-dark: #1a1418;
    --photo-mid: #5a4a48;
    --photo-light: #c9b3a8;
  }
  html, body {
    margin: 0;
    padding: 0;
    width: 1200px;
    height: 134px;
    overflow: hidden;
    background: var(--page-bg);
  }
  .banner {
    position: absolute;
    left: 10px;
    top: 9px;
    width: 1180px;
    height: 116px;
    background: var(--banner-navy);
    overflow: hidden;
  }
  .brand-name {
    position: absolute;
    left: 96px;
    top: 8px;
    margin: 0;
    font-family: "Open Sans", sans-serif;
    font-weight: 400;
    font-size: 50px;
    line-height: 60px;
    letter-spacing: 0;
    color: var(--brand-white);
    white-space: nowrap;
  }
  .tagline {
    position: absolute;
    left: 265px;
    top: 76px;
    margin: 0;
    font-family: "Open Sans", sans-serif;
    font-weight: 400;
    font-size: 27px;
    line-height: 32px;
    color: var(--brand-pink);
    white-space: nowrap;
  }
  .model-photo {
    position: absolute;
    right: 0;
    top: 0;
    width: 358px;
    height: 116px;
    background: linear-gradient(90deg, var(--banner-navy) 0%, var(--photo-dark) 14%, var(--photo-mid) 45%, var(--photo-light) 100%);
  }
</style>
</head>
<body>
  <div class="banner">
    <h1 class="brand-name">Velvo Massage</h1>
    <p class="tagline">1000,s of UK Escorts &amp; Massage Parlours</p>
    <div class="model-photo" role="img" aria-label="Close-up photograph of a woman with dark hair and green eye make-up"></div>
  </div>
</body>
</html>
```